Manufacturing company needs new business card.

I need a unique Business Card that will truly stand out. Nothing too busy. Simple is good, right? Not looking for a standard design either. No cookie cutter layout. I am just looking for something interesting and a bit different. Does't have to completely off the wall crazy, just not your run of the mill business card. Clean and modern with a touch of industrial.

Target Market(s)

Air conditioning industry, Architects, builders.

Industry/Entity Type

Business

Contact Information for Business Card

Details to be included on card are:

Peter Walsh
Managing Director

T: 1300 418 592
M: 0427 385 914
W: www.brandvalefabrication.com.au
E: peter.walsh@brandvalefabrication.com.au
A: 58 Harlow Lane, Sydney NSW 2000

Font styles to use
Sans Serif

Colors
0355a3
848484
fbfbfb

Requirements
Must have
• Card design must be landscape.

```html
<!DOCTYPE html>
<html lang="en">
<head>
<meta charset="utf-8">
<title>Brandvale Fabrication – Business Card</title>
<link rel="stylesheet" href="https://fonts.googleapis.com/css2?family=Roboto+Condensed:wght@300;400;500;700&display=swap">
<style>
  :root {
    --brand-blue: #2f4a9a;
    --brand-grey: #848484;
    --brand-light: #fbfbfb;
    --text-dark: #2a2a2a;
    --page-bg: #ebe9e5;
    --silver-1: #efefef;
    --silver-2: #ffffff;
    --silver-3: #cdcdcd;
  }
  * { box-sizing: border-box; margin: 0; padding: 0; }
  html, body {
    width: 1045px;
    height: 1200px;
    overflow: hidden;
    background: var(--page-bg);
    font-family: "Roboto Condensed", Arial, sans-serif;
  }
  .card {
    position: absolute;
    left: 95px;
    width: 856px;
    height: 496px;
    overflow: hidden;
    background: linear-gradient(90deg, var(--silver-1) 0%, var(--silver-2) 55%, var(--silver-3) 100%);
    border: 1px solid #d6d6d6;
  }
  .card--front { top: 70px; }
  .card--back { top: 650px; }
  .card__graphics { position: absolute; inset: 0; width: 100%; height: 100%; }

  .holder-name {
    position: absolute;
    left: 88px;
    top: 72px;
    font-size: 35px;
    font-weight: 700;
    letter-spacing: 0.5px;
    line-height: 1;
    text-transform: uppercase;
  }
  .holder-name__first { color: var(--brand-blue); }
  .holder-name__last { color: var(--brand-grey); }
  .holder-role {
    position: absolute;
    left: 88px;
    top: 111px;
    font-size: 24px;
    font-weight: 300;
    color: var(--brand-grey);
  }

  .company {
    position: absolute;
    display: flex;
    align-items: center;
    color: var(--brand-blue);
    font-weight: 400;
    white-space: nowrap;
  }
  .company__square { background: var(--brand-blue); flex: none; }
  .company--small { left: 455px; top: 68px; font-size: 30px; gap: 14px; }
  .company--small .company__square { width: 48px; height: 48px; }
  .company--large { left: 182px; top: 150px; font-size: 46px; gap: 22px; }
  .company--large .company__square { width: 80px; height: 80px; }

  .contact-list { list-style: none; }
  .contact-item {
    position: absolute;
    display: flex;
    align-items: center;
    gap: 12px;
    font-size: 27px;
    font-weight: 400;
    color: var(--text-dark);
    white-space: nowrap;
  }
  .contact-item__icon {
    width: 44px;
    height: 44px;
    flex: none;
    border-radius: 50%;
    background: var(--brand-blue);
    display: flex;
    align-items: center;
    justify-content: center;
  }
  .contact-item__icon svg { width: 24px; height: 24px; }
  .contact-item--phone   { left: 64px;  top: 180px; }
  .contact-item--mobile  { left: 91px;  top: 229px; }
  .contact-item--web     { left: 117px; top: 281px; }
  .contact-item--email   { left: 140px; top: 330px; }
  .contact-item--address { left: 167px; top: 379px; }

  .back-web {
    position: absolute;
    left: 310px;
    top: 276px;
    font-size: 35px;
    font-weight: 400;
    color: var(--brand-blue);
  }
</style>
</head>
<body>

<section class="card card--front" aria-label="Business card front">
  <svg class="card__graphics" viewBox="0 0 706 410" preserveAspectRatio="none" aria-hidden="true">
    <defs>
      <linearGradient id="perforated-metal" x1="0" y1="0" x2="1" y2="1">
        <stop offset="0" stop-color="#e6e6e6"/>
        <stop offset="1" stop-color="#bdbdbd"/>
      </linearGradient>
    </defs>
    <polygon points="0,18 193,410 168,410 0,68" fill="var(--brand-grey)"/>
    <polygon points="0,82 160,410 128,410 0,148" fill="var(--brand-blue)"/>
    <polygon role="img" aria-label="Perforated metal texture" points="0,168 118,410 0,410" fill="url(#perforated-metal)"/>
    <polygon points="193,410 706,340 706,410" fill="var(--brand-blue)"/>
  </svg>

  <div class="holder-name"><span class="holder-name__first">Peter</span> <span class="holder-name__last">Walsh</span></div>
  <div class="holder-role">Managing Director</div>

  <div class="company company--small"><span class="company__square"></span>Brandvale Fabrication</div>

  <ul class="contact-list">
    <li class="contact-item contact-item--phone">
      <span class="contact-item__icon"><svg viewBox="0 0 24 24"><path fill="#fff" d="M6.6 10.8a15.2 15.2 0 0 0 6.6 6.6l2.2-2.2c.3-.3.7-.4 1-.2 1.1.4 2.3.6 3.6.6.6 0 1 .4 1 1V20c0 .6-.4 1-1 1A17 17 0 0 1 3 4c0-.6.4-1 1-1h3.5c.6 0 1 .4 1 1 0 1.3.2 2.5.6 3.6.1.3 0 .7-.2 1z"/></svg></span>
      1300 418 592
    </li>
    <li class="contact-item contact-item--mobile">
      <span class="contact-item__icon"><svg viewBox="0 0 24 24"><rect x="6.5" y="2.5" width="11" height="19" rx="2" fill="none" stroke="#fff" stroke-width="1.8"/><line x1="10" y1="18.5" x2="14" y2="18.5" stroke="#fff" stroke-width="1.8"/></svg></span>
      0427 385 914
    </li>
    <li class="contact-item contact-item--web">
      <span class="contact-item__icon"><svg viewBox="0 0 24 24" fill="none" stroke="#fff" stroke-width="1.5"><circle cx="12" cy="12" r="9"/><ellipse cx="12" cy="12" rx="4" ry="9"/><line x1="3" y1="12" x2="21" y2="12"/><line x1="12" y1="3" x2="12" y2="21"/></svg></span>
      www.brandvalefabrication.com.au
    </li>
    <li class="contact-item contact-item--email">
      <span class="contact-item__icon"><svg viewBox="0 0 24 24" fill="none" stroke="#fff" stroke-width="1.6"><rect x="3" y="6" width="18" height="12" rx="1"/><polyline points="3,6 12,13 21,6"/></svg></span>
      peter.walsh@brandvalefabrication.com.au
    </li>
    <li class="contact-item contact-item--address">
      <span class="contact-item__icon"><svg viewBox="0 0 24 24"><path fill="#fff" d="M12 2a7 7 0 0 0-7 7c0 5.2 7 13 7 13s7-7.8 7-13a7 7 0 0 0-7-7zm0 9.5A2.5 2.5 0 1 1 12 6.5a2.5 2.5 0 0 1 0 5z"/></svg></span>
      58 Harlow Lane, Sydney NSW 2000
    </li>
  </ul>
</section>

<section class="card card--back" aria-label="Business card back">
  <svg class="card__graphics" viewBox="0 0 706 410" preserveAspectRatio="none" aria-hidden="true">
    <defs>
      <linearGradient id="perforated-metal-back" x1="0" y1="0" x2="1" y2="1">
        <stop offset="0" stop-color="#e6e6e6"/>
        <stop offset="1" stop-color="#bdbdbd"/>
      </linearGradient>
    </defs>
    <polygon points="0,18 193,410 168,410 0,68" fill="var(--brand-grey)"/>
    <polygon points="0,82 160,410 128,410 0,148" fill="var(--brand-blue)"/>
    <polygon role="img" aria-label="Perforated metal texture" points="0,168 118,410 0,410" fill="url(#perforated-metal-back)"/>
    <polygon points="193,410 706,340 706,410" fill="var(--brand-blue)"/>
  </svg>

  <div class="company company--large"><span class="company__square"></span>Brandvale Fabrication</div>
  <div class="back-web">www.brandvalefabrication.com.au</div>
</section>

</body>
</html>
```